Real Estate Agent needs business card design

We have logo designed already, want to have business card designed. Very interested in those smaller size business card as they look very trendy. Business name is called TOVANE REALTY

Industry/Entity Type

Business

```html
<!DOCTYPE html>
<html lang="en">
<head>
<meta charset="utf-8">
<title>Tovane Realty – Business Card</title>
<link rel="stylesheet" href="https://fonts.googleapis.com/css2?family=Cinzel:wght@600&family=Open+Sans:wght@400&display=swap">
<style>
  :root {
    --backdrop: #3b3430;
    --card-white: #fbfbfa;
    --card-dark: #2f2f31;
    --gold: #c49a5e;
    --ink: #2a2a2a;
    --text-grey: #4a4a4a;
    --white: #ffffff;
  }
  * { margin: 0; padding: 0; box-sizing: border-box; }
  html, body {
    width: 1200px;
    height: 844px;
    overflow: hidden;
    background: var(--backdrop);
  }
  .canvas {
    position: relative;
    width: 1200px;
    height: 844px;
    display: flex;
    align-items: center;
    justify-content: center;
    gap: 60px;
  }
  .card {
    position: relative;
    width: 520px;
    height: 316px;
    border-radius: 3px;
    box-shadow: 0 10px 30px rgba(0,0,0,0.35);
    overflow: hidden;
  }

  /* Front */
  .card-front { background: var(--card-white); }
  .brand {
    position: absolute;
    top: 70px;
    right: 48px;
    display: flex;
    align-items: center;
    gap: 10px;
  }
  .brand-dot {
    width: 14px;
    height: 14px;
    border-radius: 50%;
    background: var(--gold);
  }
  .brand-name {
    font-family: "Cinzel", serif;
    font-weight: 600;
    font-size: 24px;
    letter-spacing: 1px;
    color: var(--ink);
  }
  .contact {
    position: absolute;
    left: 40px;
    bottom: 36px;
    font-family: "Open Sans", sans-serif;
    color: var(--text-grey);
  }
  .agent-name {
    font-family: "Cinzel", serif;
    font-weight: 600;
    font-size: 21px;
    color: var(--gold);
    letter-spacing: 0.5px;
    line-height: 1.1;
  }
  .agent-role { font-size: 14px; line-height: 1.3; margin-bottom: 12px; }
  .address { font-size: 14px; line-height: 1.4; margin-bottom: 12px; }
  .contact-line {
    display: flex;
    align-items: center;
    gap: 8px;
    font-size: 14px;
    line-height: 1.5;
  }
  .contact-icon { width: 12px; height: 12px; flex: none; }

  /* Back */
  .card-back {
    background: var(--card-dark);
    display: flex;
    align-items: center;
    justify-content: center;
  }
  .seal {
    width: 176px;
    height: 176px;
    border-radius: 50%;
    background: var(--gold);
    display: flex;
    align-items: center;
    justify-content: center;
  }
  .seal-name {
    font-family: "Cinzel", serif;
    font-weight: 600;
    font-size: 16px;
    letter-spacing: 0.5px;
    color: var(--white);
  }
</style>
</head>
<body>
<main class="canvas">
  <section class="card card-front">
    <div class="brand">
      <span class="brand-dot"></span>
      <span class="brand-name">Tovane Realty</span>
    </div>
    <div class="contact">
      <p class="agent-name">Helena Brooks</p>
      <p class="agent-role">Senior Property Consultant</p>
      <p class="address">7C, 48 Harbour Street,<br>Westmere, NSW 2199</p>
      <p class="contact-line">
        <svg class="contact-icon" viewBox="0 0 24 24" aria-hidden="true"><path fill="#c49a5e" d="M6.6 10.8a15.1 15.1 0 0 0 6.6 6.6l2.2-2.2c.3-.3.7-.4 1-.2 1.1.4 2.3.6 3.6.6.6 0 1 .4 1 1V20c0 .6-.4 1-1 1A17 17 0 0 1 3 4c0-.6.4-1 1-1h3.5c.6 0 1 .4 1 1 0 1.3.2 2.5.6 3.6.1.3 0 .7-.2 1z"/></svg>
        0400 123 987
      </p>
      <p class="contact-line">
        <svg class="contact-icon" viewBox="0 0 24 24" aria-hidden="true"><circle cx="12" cy="12" r="10" fill="#c49a5e"/><path d="M2 12h20M12 2c3 3 3 17 0 20M12 2c-3 3-3 17 0 20" stroke="#fbfbfa" stroke-width="1.5" fill="none"/></svg>
        www.tovanerealty.com.au
      </p>
    </div>
  </section>

  <section class="card card-back">
    <div class="seal">
      <span class="seal-name">Tovane Realty</span>
    </div>
  </section>
</main>
</body>
</html>
```